KWT Website revamping

Make a website main page, navigation / menu options, couple of product pages in the 4 product categories, improvement on About us.
Our Website will need to be in PHP.
Our competitors websites for an idea.
www.morvado.example
https://heatwise.example/en-gb/brands/trovani
www.lumbra.example
www.sidra.example
Our website is temporarily hosted at https://www.brightfoldweb.example/kwt/
Once done, we would like a quote for coding the entire website as well. If we find the quote good we will go ahead with you.

Target Market(s)

Industrial and Commercial Refrigeration , Cold Store, freezer and chiller manufacturers and commercial Airconditioning contractors and Industrial Automation panel makers.

Industry/Entity Type

Engineering

Number of Pages Required

5+ page

Font styles to use
Other font styles liked:
• "Michroma" "Roboto" "MONTSERRAT"

Colors
3377b5
ffffff

Requirements
Must have
• Main page, index/menu, couple of product pages.
Nice to have
• A good navigation to the product list
Font should be similar to the top menu line
Showcase our site as a good electronics temperature controller manufacturer for Refrigeration / Industrial Process Automation

```html
<!DOCTYPE html>
<html lang="en">
<head>
<meta charset="utf-8">
<title>BRIGHTFOLD – Electronic Temperature Controllers</title>
<link href="https://fonts.googleapis.com/css2?family=Montserrat:wght@300;400;500;600;700;800&display=swap" rel="stylesheet">
<style>
:root{
  --brand:#3377b5;
  --brand-deep:#1f4f9c;
  --navy:#1b3f86;
  --topbar:#dde6f2;
  --white:#ffffff;
  --ink:#2b2b2b;
  --muted:#777d86;
  --section:#e7edf5;
  --footer:#2e63ab;
  --footer-base:#3a6cb2;
}
*{margin:0;padding:0;box-sizing:border-box}
html,body{width:1200px;height:3745px;overflow:hidden}
body{position:relative;background:var(--white);font-family:"Montserrat",sans-serif;color:var(--ink)}
.abs{position:absolute}
a{color:inherit;text-decoration:none}

.topbar{left:0;top:0;width:1200px;height:44px;background:var(--topbar);font-size:12px;color:var(--navy)}
.topbar .item{position:absolute;top:15px;display:flex;align-items:center;gap:6px}
.nav{left:0;top:44px;width:1200px;height:104px;background:var(--white)}
.logo{position:absolute;left:90px;top:37px;font-size:29px;font-weight:700;color:var(--brand);letter-spacing:.5px}
.menu a{position:absolute;top:44px;font-size:15px;font-weight:500;color:#333}
.menu a.active{color:var(--navy)}

.hero{left:0;top:148px;width:1200px;height:612px}
.hero-photo{position:absolute;inset:0;background:linear-gradient(160deg,#cfd8e3 0%,#8e9aa8 40%,#b9c3cf 65%,#6f7986 100%)}
.hero-box{left:96px;top:298px;width:486px;height:259px;background:rgba(51,119,181,.88);color:var(--white);padding:40px 0 0 44px}
.hero-box h1{font-size:33px;font-weight:800;line-height:36px;letter-spacing:.3px}
.hero-box p{font-size:28px;font-weight:400;margin-top:4px}
.pill{display:inline-flex;align-items:center;justify-content:center;gap:6px;border-radius:30px;font-size:15px;font-weight:600}
.pill.solid{background:var(--white);color:var(--brand-deep)}
.pill.outline{border:2px solid var(--brand-deep);color:var(--brand-deep)}
.pill.ghost{border:2px solid var(--white);color:var(--white)}
.arrow{width:40px;height:40px;border-radius:50%;background:rgba(255,255,255,.9);display:flex;align-items:center;justify-content:center}
.dotline{width:2px;border-left:2px dotted #333}
.dot{width:7px;height:7px;border-radius:50%;background:#222}

.about h2{font-size:34px;font-weight:400;color:var(--navy)}
.about h2 b{font-weight:800}
.about p{font-size:15px;line-height:25px;color:var(--muted);width:540px;margin-bottom:14px}

.tile{top:1321px;width:396px;height:407px;color:var(--white);text-align:center}
.tile .ph{position:absolute;inset:0}
.tile .ph::after{content:"";position:absolute;inset:0;background:rgba(0,0,0,.25)}
.tile h3{position:absolute;top:213px;width:100%;font-size:25px;font-weight:800;z-index:1}
.tile p{position:absolute;top:253px;width:100%;font-size:14px;line-height:25px;z-index:1}
.tile .pill{position:absolute;top:315px;left:110px;width:176px;height:49px;z-index:1}

.products-bg{left:0;top:1728px;width:1200px;height:522px;background:var(--section)}
.center-title{width:1200px;text-align:center;font-size:30px;font-weight:800;color:var(--navy)}
.center-text{width:1200px;text-align:center;font-size:15px;line-height:25px;color:#333}
.prod{top:1945px;width:320px;height:232px;color:var(--white)}
.prod span{position:absolute;left:20px;bottom:18px;font-size:16px;font-weight:800;line-height:20px}

.feature{left:0;top:2250px;width:1200px;height:510px;background:linear-gradient(120deg,#1a4aa5 0%,#2a6ec8 60%,#3b8ad8 100%);color:var(--white)}
.feature h2{position:absolute;left:112px;top:113px;font-size:25px;font-weight:400;line-height:36px}
.feature h2 b{font-weight:800}
.feature p{position:absolute;left:114px;font-size:15px;line-height:25px;width:410px}

.news-title{left:150px;top:2843px;font-size:29px;font-weight:400;color:var(--navy)}
.news-title b{font-weight:800}
.card{top:2906px;width:279px;height:365px;background:var(--white);box-shadow:0 3px 14px rgba(0,0,0,.12)}
.card .img{height:165px}
.card .body{padding:21px 28px 0}
.card .date{font-size:11px;font-weight:700;color:var(--navy)}
.card h4{font-size:14px;font-weight:700;color:#333;line-height:19px;margin-top:11px;text-transform:uppercase}
.card p{font-size:11px;line-height:17.5px;color:var(--muted);margin-top:10px}
.card .more{display:block;font-size:11px;font-weight:700;color:var(--brand);margin-top:11px}

.footer{left:0;top:3351px;width:1200px;height:333px;background:var(--footer);color:var(--white)}
.footer .brand{position:absolute;left:151px;top:84px;font-size:27px;font-weight:400;letter-spacing:.5px}
.footer .desc{position:absolute;left:151px;top:140px;width:240px;font-size:11.5px;line-height:19px;color:#cfdcef}
.footer .col{position:absolute;top:75px}
.footer .col h5{font-size:17px;font-weight:500;margin-bottom:16px}
.footer .col li{list-style:none;font-size:13px;height:29px;display:flex;align-items:flex-start;gap:10px}
.footer .col li .ic{width:18px;flex:none;display:flex;justify-content:center}
.social{position:absolute;top:3562px;width:34px;height:34px;border:1.5px solid var(--white);border-radius:50%}
.base{left:0;top:3684px;width:1200px;height:61px;background:var(--footer-base);text-align:center;font-size:12px;color:#b9cbe6;padding-top:22px}
</style>
</head>
<body>

<div class="abs topbar">
  <span class="item" style="left:93px">
    <svg width="14" height="14" viewBox="0 0 24 24" fill="none" stroke="#1b3f86" stroke-width="2.2"><path d="M5 3h4l2 5-3 2a12 12 0 0 0 6 6l2-3 5 2v4a2 2 0 0 1-2 2A17 17 0 0 1 3 5a2 2 0 0 1 2-2z"/></svg>(555) 014 2252
  </span>
  <span class="item" style="left:226px">
    <svg width="16" height="12" viewBox="0 0 24 18" fill="#1b3f86"><path d="M0 0h24v18H0z"/><path d="M0 0l12 9 12-9" stroke="#dde6f2" stroke-width="2" fill="none"/></svg>hello@brightfold.example
  </span>
  <span class="item" style="left:1030px">
    <svg width="15" height="15" viewBox="0 0 24 24" fill="none" stroke="#1b3f86" stroke-width="3"><circle cx="10" cy="10" r="7"/><path d="M15 15l7 7"/></svg>SEARCH HERE
  </span>
</div>

<div class="abs nav">
  <div class="logo">BRIGHTFOLD</div>
  <nav class="menu">
    <a class="active" style="left:369px">ABOUT US</a>
    <a style="left:489px">SERVICES</a>
    <a style="left:599px">PRODUCTS</a>
    <a style="left:723px">SOLUTION</a>
    <a style="left:842px">INDUSTRIES</a>
    <a style="left:973px">NEWS</a>
    <a style="left:1060px">CONTACT</a>
  </nav>
</div>

<section class="abs hero">
  <div class="hero-photo" role="img" aria-label="Rooftop industrial refrigeration units with large silver ducting under a grey sky"></div>
  <svg class="abs" style="left:0;top:540px" width="1200" height="80" viewBox="0 0 1200 80">
    <path d="M0 0 Q600 75 1200 0 V80 H0Z" fill="#fff"/>
    <path d="M0 0 Q600 75 1200 0 L1200 4 Q600 82 0 4Z" fill="#2a62b0"/>
  </svg>
</section>
<div class="abs hero-box">
  <h1>WE DO INUDSTRIAL<br>REFRIGERATION</h1>
  <p>TEMPERATURE CONTROLLER</p>
</div>
<a class="abs pill solid" style="left:140px;top:465px;width:186px;height:50px">LEARN MORE ›</a>
<div class="abs arrow" style="left:36px;top:389px"><svg width="12" height="18" viewBox="0 0 12 18"><path d="M10 1L2 9l8 8" stroke="#222" stroke-width="2.5" fill="none"/></svg></div>
<div class="abs arrow" style="left:1124px;top:389px"><svg width="12" height="18" viewBox="0 0 12 18"><path d="M2 1l8 8-8 8" stroke="#222" stroke-width="2.5" fill="none"/></svg></div>
<div class="abs dotline" style="left:598px;top:768px;height:86px"></div>
<div class="abs dot" style="left:596px;top:854px"></div>

<div class="abs" role="img" aria-label="Digital temperature controller units with LED displays and a touch control panel" style="left:93px;top:905px;width:457px;height:290px;border-radius:14px;background:linear-gradient(135deg,#2a2c31 0%,#8a8e95 40%,#3a3d43 70%,#1f2126 100%)"></div>
<section class="abs about" style="left:611px;top:915px">
  <h2>ABOUT <b>BRIGHTFOLD</b></h2>
  <div style="margin-top:30px">
    <p>Aonsectetuer augue nisi quis lacus Ut ac mi quis lacus mollis aliquam Curabitur iaculis tempus eros Curabitur vel mi sit amet magna malesuada ultrices Ut nisi erat fermentum</p>
    <p>Fusce ultricies orci ac feugiat suscipit leo massa sodales velit et scelerisque mi tortor at ipsum Proin orci odio commodo ac gravida non tristique vel tellus Pellentesque nibh libero ultricies eu sagittis</p>
  </div>
</section>
<a class="abs pill outline" style="left:608px;top:1172px;width:177px;height:50px">LEARN MORE ›</a>

<div class="abs tile" style="left:0">
  <div class="ph" role="img" aria-label="Industrial plant with blue pipework and air handling equipment" style="background:linear-gradient(180deg,#6e9dc4,#52798f 60%,#7d8e95)"></div>
  <h3>OUR PRODUCTS</h3>
  <p>Praesent sit amet est In dictum dolor eu<br>dictum porttitor enim felis</p>
  <a class="pill ghost">LEARN MORE ›</a>
</div>
<div class="abs tile" style="left:400px">
  <div class="ph" role="img" aria-label="Abstract glowing blue digital technology artwork" style="background:radial-gradient(circle at 45% 55%,#f3a04b 0%,#3d7ad8 30%,#13307a 70%,#0c1a4d)"></div>
  <h3>TECHNOLOGY</h3>
  <p>Praesent sit amet est In dictum dolor eu<br>dictum porttitor enim felis</p>
  <a class="pill ghost">LEARN MORE ›</a>
</div>
<div class="abs tile" style="left:804px">
  <div class="ph" role="img" aria-label="Row of outdoor condenser fan units" style="background:linear-gradient(180deg,#b8bcc0,#8f9499 60%,#6d7276)"></div>
  <h3>OUR SOLUTION</h3>
  <p>Praesent sit amet est In dictum dolor eu<br>dictum porttitor enim felis</p>
  <a class="pill ghost">LEARN MORE ›</a>
</div>

<div class="abs products-bg"></div>
<div class="abs dotline" style="left:598px;top:1728px;height:40px"></div>
<div class="abs dot" style="left:596px;top:1768px"></div>
<h2 class="abs center-title" style="left:0;top:1806px">OUR PRODUCTS</h2>
<p class="abs center-text" style="left:0;top:1856px">Praesent sit amet est In dictum dolor eu dictum porttitor enim felis viverra mi eget luctus massa purus quis odio<br>Etiam nulla massa pharetra facilisis volutpat in imperdiet sit amet sem Aliquam nec erat at</p>
<div class="abs prod" style="left:100px" role="img" aria-label="Air conditioning controller with red digital display on a blue background"><div style="position:absolute;inset:0;background:linear-gradient(135deg,#2f7fd6,#6fb1ec 55%,#3a86d8)"></div><span>AIR CONDITIONING<br>CONTROLLER</span></div>
<div class="abs prod" style="left:432px" role="img" aria-label="Refrigeration controller unit on a blue background"><div style="position:absolute;inset:0;background:linear-gradient(135deg,#2f7fd6,#6fb1ec 55%,#3a86d8)"></div><span>REFRIGERATION<br>CONTROLLER</span></div>
<div class="abs prod" style="left:761px" role="img" aria-label="Industrial process automation device on a blue background"><div style="position:absolute;inset:0;background:linear-gradient(135deg,#2f7fd6,#6fb1ec 55%,#3a86d8)"></div><span>INDUSTRIAL PROCESS<br>AUTOMATION</span></div>

<section class="abs feature">
  <div class="abs" role="img" aria-label="Stainless steel commercial cold room kitchen interior" style="left:545px;top:0;width:655px;height:510px;clip-path:polygon(112px 0,655px 0,655px 510px,112px 510px,0 244px);background:linear-gradient(160deg,#9ea5ad,#d4d8dc 45%,#7d848c)"></div>
  <svg class="abs" style="left:545px;top:0" width="120" height="510" viewBox="0 0 120 510"><path d="M112 0 L0 244 L112 510" stroke="#ffffff" stroke-opacity=".35" stroke-width="6" fill="none"/></svg>
  <h2>ELECTRONICS TEMPERATURE<br><b>CONTROLLER MANUFACTURER</b></h2>
  <p style="top:192px">Praesent sit amet est In dictum dolor eu dictum porttitor enim felis viverra mi eget</p>
  <p style="top:254px">Auis odio Etiam nulla massa pharetra facilisis volutpat in imperdiet sit amet sem Aliquam nec erat at purus cursus interdum Vestibulum ligula</p>
  <a class="abs pill ghost" style="left:112px;top:354px;width:177px;height:46px">LEARN MORE ›</a>
</section>

<h2 class="abs news-title">LATEST <b>NEWS</b></h2>
<svg class="abs" style="left:996px;top:2850px" width="56" height="22" viewBox="0 0 56 22"><path d="M13 3l-8 8 8 8" stroke="#bbb" stroke-width="2.5" fill="none"/><path d="M42 3l8 8-8 8" stroke="#333" stroke-width="2.5" fill="none"/></svg>

<article class="abs card" style="left:147px">
  <div class="img" role="img" aria-label="Cold storage aisle with metal shelving" style="background:linear-gradient(180deg,#a9c4e2,#5d87b8)"></div>
  <div class="body">
    <div class="date">JAN 20, 2020</div>
    <h4>Curabitur iaculis tempus eros curabitur vel</h4>
    <p>Curabitur vel dolor ultrices ipsum dictum tristique Praesent vitae lacus Ut velit enim vestibulum non fermentum</p>
    <a class="more">LEARN MORE ›</a>
  </div>
</article>
<article class="abs card" style="left:464px">
  <div class="img" role="img" aria-label="Close-up of a metal fan grille" style="background:radial-gradient(circle at 45% 55%,#e8eef5,#8fa0b3 60%,#5d6d80)"></div>
  <div class="body">
    <div class="date">JAN 15, 2020</div>
    <h4>Nunc tempus felis vitae urna vivamus</h4>
    <p>Curabitur vel dolor ultrices ipsum dictum tristique Praesent vitae lacus Ut velit enim vestibulum non fermentum</p>
    <a class="more">LEARN MORE ›</a>
  </div>
</article>
<article class="abs card" style="left:780px">
  <div class="img" role="img" aria-label="Stainless steel commercial refrigerator cabinets" style="background:linear-gradient(90deg,#6f757c,#b7bcc2 50%,#7b8188)"></div>
  <div class="body">
    <div class="date">JAN 10, 2020</div>
    <h4>Praesent sit amet est in dictum dolor dictu</h4>
    <p>Curabitur vel dolor ultrices ipsum dictum tristique Praesent vitae lacus Ut velit enim vestibulum non fermentum</p>
    <a class="more">LEARN MORE ›</a>
  </div>
</article>

<footer class="abs footer">
  <div class="brand">BRIGHTFOLD</div>
  <p class="desc">Curabitur vel dolor ultrices ipsum dictum tristique Praesent vitae lacus Ut velit enim vestibulum non</p>
  <div class="col" style="left:451px"><h5>COMPANY</h5><ul><li>About Us</li><li>Services</li><li>Our Data Centers</li><li>Industries</li></ul></div>
  <div class="col" style="left:617px"><h5>RESOURCES</h5><ul><li>Air Conditioning Controller</li><li>Refrigeration Controller</li><li>Industrial Process Automation</li><li>Contact Us</li></ul></div>
  <div class="col" style="left:863px"><h5>CONTACT US</h5>
    <ul>
      <li><span class="ic"><svg width="16" height="20" viewBox="0 0 16 20"><path d="M8 0a7 7 0 0 1 7 7c0 5-7 13-7 13S1 12 1 7a7 7 0 0 1 7-7z" fill="#fff"/><circle cx="8" cy="7" r="2.6" fill="#2e63ab"/></svg></span>48 Harbor Lane #4B</li>
      <li><span class="ic"></span>Lakeview 55021 NV</li>
      <li><span class="ic"><svg width="17" height="17" viewBox="0 0 24 24" fill="none" stroke="#fff" stroke-width="2.2"><path d="M5 3h4l2 5-3 2a12 12 0 0 0 6 6l2-3 5 2v4a2 2 0 0 1-2 2A17 17 0 0 1 3 5a2 2 0 0 1 2-2z"/></svg></span>(555) 014 2252</li>
      <li><span class="ic"><svg width="18" height="13" viewBox="0 0 24 18" fill="#fff"><path d="M0 0h24v18H0z"/><path d="M0 0l12 9 12-9" stroke="#2e63ab" stroke-width="2" fill="none"/></svg></span>hello@brightfold.example</li>
    </ul>
  </div>
</footer>
<span class="social" style="left:151px" aria-label="Social link"></span>
<span class="social" style="left:191px" aria-label="Social link"></span>
<span class="social" style="left:231px" aria-label="Social link"></span>
<span class="social" style="left:271px" aria-label="Social link"></span>
<div class="abs base">© 2020 Company Name | All Rights Reserved | Disclaimer</div>

</body>
</html>
```